Core values in our company OTK (Oversight and Transit Keepers)

Do good:
1. Being Direct and communicative for the benefit of all parties
2. Working for the Benefit of the company, client and team members
3. Wanting to improve to create a better impact
4. Having healthy rivalry
Be ahead of curve:
1. Having the confidence to break through barriers which arise
2. Desire to grow and learn towards establishment and agreed goal
3. Getting off the sidelines and get into the game
4. Keeping the end game in mind having due regard to processes and milestones
5. Self starter and works on own initiative
6. Diligent and impactful in your field of responsibility
Truth and Honesty
2. Have the confidence and ability to speak what you really want to communicate
3. Being truthful to yourself, clients and colleagues to find the innovations that lie within
4. Seeking the truth by opening things up for discussion
5. Being Optimistic
Background Information on our Company:OTK is a professional law firm in London Docklands. We caters for both private and corporate clients ranging from highly regarded and established law firms to boutique and niche immigration practices. We also specialises in expert legal advice and prides itself on providing services that go beyond the expectations of its clients.
What we need: We need a Poster about Truth and Honesty, this is to show one of our values as a company. It will need to be vibrant and straight to the point. Colours can be orange grey white and yellow. Attached is our company logo.
Reason: To remind colleagues that this is one of our main values and it is instilled in our company.
Things we would like:
1. To create a point of focus
2. Use shapes to create visual interest
3. Use creative illustrations
4. Take the viewer’s focus on a journey with clever perspective
Industry/Entity Type
Legal
Requirements
Must have
- a globe (Picture)
- Do good:
- 1. Being Direct and communicative for the benefit of all parties
- 2. Working for the Benefit of the company, client and team members
- 3. Wanting to improve to create a better impact
- 4. Having healthy rivalry
- Be ahead of curve:
- 1. Having the confidence to break through barriers which arise
- 2. Desire to grow and learn towards establishment and agreed goal
- 3. Getting off the sidelines and get into the game
- 4. Keeping the end game in mind having due regard to processes and milestones
- 5. Self starter and works on own initiative
- 6. Diligent and impactful in your field of responsibility
- Truth and Honesty
- 2. Have the confidence and ability to speak what you really want to communicate
- 3. Being truthful to yourself, clients and colleagues to find the innovations that lie within
- 4. Seeking the truth by opening things up for discussion
- 5. Being Optimistic

```html
<!DOCTYPE html>
<html lang="en">
<head>
<meta charset="utf-8">
<title>OTK Poster – Truth and Honesty</title>
<link href="https://fonts.googleapis.com/css2?family=Libre+Baskerville:wght@400;700&family=Montserrat:wght@400;600;700;900&display=swap" rel="stylesheet">
<style>
  :root{
    --orange:#f07a1a;
    --orange-deep:#e2630c;
    --charcoal:#444446;
    --ink:#2b2b2b;
    --grey-light:#efefef;
    --grey-mid:#d4d4d4;
    --stage:#cfcfcf;
    --white:#ffffff;
  }
  *{margin:0;padding:0;box-sizing:border-box}
  html,body{width:1200px;height:2163px;overflow:hidden;background:var(--stage)}
  .poster{position:absolute;left:48px;top:302px;width:1104px;height:1559px;background:var(--white);box-shadow:0 12px 40px rgba(0,0,0,.25);overflow:hidden}
  .poster-shapes{position:absolute;inset:0}
  .brand{position:absolute;top:30px;left:0;width:100%;text-align:center}
  .brand-name{font-family:"Libre Baskerville",serif;font-weight:700;font-size:86px;color:var(--orange);line-height:1}
  .brand-tagline{font-family:"Libre Baskerville",serif;font-size:17px;color:var(--charcoal);margin-top:6px}
  .intro{position:absolute;left:54px;top:838px;width:362px;font-family:"Montserrat",sans-serif;font-size:17.5px;line-height:1.5;color:var(--ink);text-align:justify}
  .intro p+p{margin-top:18px}
  .intro strong{font-weight:700}
  .consult{position:absolute;left:83px;top:1152px;width:280px;height:280px;display:flex;flex-direction:column;align-items:center;justify-content:center;font-family:"Montserrat",sans-serif;text-align:center}
  .consult-free{font-weight:900;font-size:50px;color:var(--ink);line-height:.95}
  .consult-label{font-weight:700;font-size:19px;color:var(--ink);letter-spacing:.5px}
  .consult-icon{margin:8px 0 4px}
  .consult-phone{font-weight:700;font-size:28px;color:var(--white)}
  .headline{position:absolute;left:535px;top:800px;font-family:"Libre Baskerville",serif;color:var(--ink)}
  .headline-kicker{font-size:30px;font-weight:400}
  .headline-main{font-size:37px;font-weight:700;letter-spacing:.5px;margin-top:6px;white-space:nowrap}
  .pill{position:absolute;left:484px;top:922px;width:487px;height:88px;background:linear-gradient(var(--orange),var(--orange-deep));border-radius:0 26px 26px 0;box-shadow:0 8px 14px rgba(0,0,0,.18);display:flex;align-items:center;padding-left:48px;font-family:"Libre Baskerville",serif;font-weight:700;font-size:23px;color:var(--white)}
  .points{position:absolute;left:540px;top:1064px;width:520px;list-style:none;font-family:"Montserrat",sans-serif;font-weight:600;font-size:18.5px;line-height:1.4;color:var(--ink)}
  .points li{position:relative;padding-left:42px;margin-bottom:26px}
  .points li svg{position:absolute;left:0;top:3px}
  .site{position:absolute;left:0;bottom:22px;width:100%;text-align:center;font-family:"Montserrat",sans-serif;font-size:34px;color:var(--white);display:flex;justify-content:center;align-items:center;gap:10px}
</style>
</head>
<body>
<main class="poster">
  <svg class="poster-shapes" width="1104" height="1559" viewBox="0 0 1104 1559">
    <defs>
      <linearGradient id="header-fill" x1="0" y1="0" x2="0" y2="1"><stop offset="0" stop-color="#d6d6d6"/><stop offset="1" stop-color="#f7f7f7"/></linearGradient>
      <linearGradient id="photo-fill" x1="0" y1="0" x2="1" y2="1"><stop offset="0" stop-color="#e9eef2"/><stop offset=".5" stop-color="#b9c2cb"/><stop offset="1" stop-color="#3e4650"/></linearGradient>
      <linearGradient id="panel-fill" x1="0" y1="0" x2="1" y2="0"><stop offset="0" stop-color="#f4f4f4"/><stop offset="1" stop-color="#dedede"/></linearGradient>
      <linearGradient id="badge-fill" x1="0" y1="0" x2="0" y2="1"><stop offset="0" stop-color="#f68a2a"/><stop offset="1" stop-color="#e2630c"/></linearGradient>
      <radialGradient id="globe-fill" cx=".4" cy=".4" r=".7"><stop offset="0" stop-color="#f3f3f3"/><stop offset="1" stop-color="#dcdcdc"/></radialGradient>
      <filter id="soft-shadow" x="-20%" y="-20%" width="140%" height="140%"><feDropShadow dx="0" dy="8" stdDeviation="10" flood-opacity=".25"/></filter>
    </defs>
    <rect class="photo" x="0" y="120" width="1104" height="640" fill="url(#photo-fill)" role="img" aria-label="Photo of business people shaking hands over a contract on a desk"/>
    <path class="header" d="M0 0H1104V140Q560 240 0 150Z" fill="url(#header-fill)"/>
    <path d="M0 152Q560 242 1104 142" fill="none" stroke="var(--orange)" stroke-width="7"/>
    <path d="M0 168Q560 258 1104 158" fill="none" stroke="var(--charcoal)" stroke-width="9"/>
    <path class="content-bg" d="M0 770Q500 700 1104 705V1559H0Z" fill="var(--white)"/>
    <circle class="globe" cx="930" cy="1240" r="170" fill="url(#globe-fill)" opacity=".7" role="img" aria-label="Picture of a globe"/>
    <path d="M0 752Q500 682 1104 688" fill="none" stroke="var(--charcoal)" stroke-width="7"/>
    <path d="M0 768Q500 698 1104 703" fill="none" stroke="var(--orange)" stroke-width="8"/>
    <path class="side-panel" d="M0 775Q240 742 478 737V1330Q478 1450 350 1478L0 1490Z" fill="url(#panel-fill)" filter="url(#soft-shadow)"/>
    <circle cx="223" cy="1292" r="160" fill="var(--white)" filter="url(#soft-shadow)"/>
    <circle cx="223" cy="1292" r="140" fill="url(#badge-fill)"/>
    <path d="M0 1485Q552 1425 1104 1452" fill="none" stroke="var(--charcoal)" stroke-width="10"/>
    <path class="footer" d="M0 1500Q552 1445 1104 1470V1559H0Z" fill="var(--orange)"/>
  </svg>

  <header class="brand">
    <div class="brand-name">OTK</div>
    <div class="brand-tagline">oversight and transit keepers</div>
  </header>

  <section class="intro">
    <p><strong>OTK</strong> is a professional law firm in London Docklands. We caters for both private and corporate clients ranging from highly regarded and established law firms to boutique and niche immigration practices.</p>
    <p>We also specialises in expert legal advice and prides itself on providing services that go beyond the expectations of its clients.</p>
  </section>

  <div class="consult">
    <div class="consult-free">FREE</div>
    <div class="consult-label">CONSULTING</div>
    <svg class="consult-icon" width="30" height="30" viewBox="0 0 24 24"><circle cx="12" cy="12" r="10.5" fill="none" stroke="#2b2b2b" stroke-width="2"/><path d="M8.5 7c.6-.4 1.2 0 1.5.8l.6 1.5c.2.5 0 1-.4 1.3l-.6.4c.5 1.3 1.5 2.3 2.8 2.8l.4-.6c.3-.4.8-.6 1.3-.4l1.5.6c.8.3 1.2.9.8 1.5-.8 1.2-2 1.6-3.3 1.1-2.6-1-4.5-2.9-5.5-5.5C7.4 9 7.8 7.8 8.5 7z" fill="#2b2b2b"/></svg>
    <div class="consult-phone">+ 01 2040 5517</div>
  </div>

  <div class="headline">
    <div class="headline-kicker">Our core value is</div>
    <div class="headline-main">TRUTH AND HONESTY</div>
  </div>

  <div class="pill">Speak what you really mean.</div>

  <ul class="points">
    <li><svg width="24" height="24" viewBox="0 0 24 24"><circle cx="12" cy="12" r="10" fill="none" stroke="#2b2b2b" stroke-width="2"/><path d="M7 12l3.5 3.5L18 8" fill="none" stroke="#2b2b2b" stroke-width="2.4"/></svg>Have the confidence and ability to speak what you really want to communicate</li>
    <li><svg width="24" height="24" viewBox="0 0 24 24"><circle cx="12" cy="12" r="10" fill="none" stroke="#2b2b2b" stroke-width="2"/><path d="M7 12l3.5 3.5L18 8" fill="none" stroke="#2b2b2b" stroke-width="2.4"/></svg>Being truthful to yourself, clients and colleagues to find the innovations that lie within</li>
    <li><svg width="24" height="24" viewBox="0 0 24 24"><circle cx="12" cy="12" r="10" fill="none" stroke="#2b2b2b" stroke-width="2"/><path d="M7 12l3.5 3.5L18 8" fill="none" stroke="#2b2b2b" stroke-width="2.4"/></svg>Seeking the truth by opening things up for discussion</li>
    <li><svg width="24" height="24" viewBox="0 0 24 24"><circle cx="12" cy="12" r="10" fill="none" stroke="#2b2b2b" stroke-width="2"/><path d="M7 12l3.5 3.5L18 8" fill="none" stroke="#2b2b2b" stroke-width="2.4"/></svg>Being Optimistic</li>
  </ul>

  <footer class="site">
    <svg width="26" height="26" viewBox="0 0 24 24"><circle cx="12" cy="12" r="10" fill="none" stroke="#fff" stroke-width="2"/><ellipse cx="12" cy="12" rx="4.5" ry="10" fill="none" stroke="#fff" stroke-width="1.6"/><path d="M2 12h20M4 7h16M4 17h16" stroke="#fff" stroke-width="1.6"/></svg>
    www.otkkeepers.com
  </footer>
</main>
</body>
</html>
```